Business card design for Virtual Assistance company

I need a business card designed for my virtual assistance company. We are a small company who services primarily C-level executive clients. The card needs to be double sided with the following contact information on the back:
Melanie Hartwick
Owner/CEO
info@pbtadvisory.net
www.pbtadvisory.net
240.395.2817

The front side should just have the company name incorporated: "PBT Advisory" and "virtual assistance"

The card should be simplistic, but eye catching and should speak to high level executives. Our primary focus areas consist of executive assistance and government contracting.

Target Market(s)

CEOs and executives

Contact Information for Business Card

see project description. phone, email, website.

Colors

Designer to choose only greyscale colors for use in the design.

```html
<!DOCTYPE html>
<html lang="en">
<head>
<meta charset="utf-8">
<title>PBT Advisory – Business Card</title>
<link rel="stylesheet" href="https://fonts.googleapis.com/css2?family=Open+Sans:wght@400;700&display=swap">
<style>
  :root {
    --ink: #231f20;
    --paper: #ffffff;
    --backdrop: #e6e6e6;
    --edge: #b9b9b9;
  }
  * { margin: 0; padding: 0; box-sizing: border-box; }
  html, body {
    width: 1022px;
    height: 1200px;
    overflow: hidden;
    background: var(--backdrop);
    font-family: "Open Sans", Arial, sans-serif;
  }
  .sheet {
    position: relative;
    width: 1022px;
    height: 1200px;
  }
  .card {
    position: absolute;
    left: 101px;
    width: 820px;
    height: 500px;
    overflow: hidden;
  }
  .card--front { top: 70px; background: var(--paper); border: 1px solid var(--edge); }
  .card--back  { top: 630px; background: var(--ink); }
  .card svg { position: absolute; inset: 0; display: block; }

  .brand-mark,
  .tagline {
    position: absolute;
    color: var(--paper);
    text-align: center;
    white-space: nowrap;
  }
  .brand-mark { font-weight: 700; letter-spacing: 0.1em; }
  .tagline {
    font-weight: 400;
    text-transform: uppercase;
    letter-spacing: 0.25em;
  }

  .card--front .brand-mark {
    left: 10px;
    width: 380px;
    top: 352px;
    font-size: 36px;
  }
  .card--front .tagline {
    left: 10px;
    width: 380px;
    top: 420px;
    font-size: 17px;
  }
  .card--back .brand-mark {
    left: 0;
    width: 100%;
    top: 208px;
    font-size: 38px;
  }
  .card--back .tagline {
    left: 0;
    width: 100%;
    top: 268px;
    font-size: 16px;
  }

  .contact {
    position: absolute;
    right: 42px;
    text-align: right;
    color: var(--ink);
  }
  .contact__name { top: 30px; font-size: 33px; font-weight: 400; }
  .contact__role { top: 74px; font-size: 31px; font-weight: 700; }
  .contact__phone {
    top: 342px;
    font-size: 30px;
    font-weight: 700;
    display: flex;
    align-items: center;
    gap: 10px;
  }
  .contact__phone svg { position: static; width: 34px; height: 34px; }
  .contact__email { top: 392px; font-size: 25px; }
  .contact__web   { top: 428px; font-size: 25px; }
</style>
</head>
<body>
<main class="sheet">

  <section class="card card--front" aria-label="Business card, contact side">
    <svg viewBox="0 0 820 500" width="820" height="500" aria-hidden="true">
      <path d="M0 0 H349 Q610 270 354 500 H0 Z" fill="var(--ink)"/>
      <path d="M333 0 Q590 270 338 500" fill="none" stroke="var(--paper)" stroke-width="5"/>
      <circle cx="206" cy="175" r="112" fill="none" stroke="var(--paper)" stroke-width="6"/>
    </svg>
    <div class="brand-mark">PBT Advisory</div>
    <div class="tagline">Virtual Assistance</div>

    <p class="contact contact__name">Melanie Hartwick</p>
    <p class="contact contact__role">Owner/CEO</p>
    <p class="contact contact__phone">
      <svg viewBox="0 0 34 34" aria-hidden="true">
        <circle cx="17" cy="17" r="17" fill="var(--ink)"/>
        <path d="M11 9 l4 0 l1.5 5 l-2.5 2 q2 4 5 5 l2 -2.5 l5 1.5 l0 4 q-1 2 -3 2 q-14 -2 -15 -15 q0 -2 3 -2 z" fill="var(--paper)"/>
      </svg>
      <span>240.395.2817</span>
    </p>
    <p class="contact contact__email">info@pbtadvisory.net</p>
    <p class="contact contact__web">www.pbtadvisory.net</p>
  </section>

  <section class="card card--back" aria-label="Business card, brand side">
    <svg viewBox="0 0 820 500" width="820" height="500" aria-hidden="true">
      <circle cx="410" cy="250" r="190" fill="none" stroke="var(--paper)" stroke-width="8"/>
    </svg>
    <div class="brand-mark">PBT Advisory</div>
    <div class="tagline">Virtual Assistance</div>
  </section>

</main>
</body>
</html>
```